Professional business cards for real estate development company

I need business cards for my new real estate development company. The company, "KORVA" is a real estate development, investment, and advisory firm with a focus on multifamily, office, and mixed-use projects across primary and secondary markets in the Southeast United States.

Style preference is modern

Industry/Entity Type

Real Estate Development

Contact Information for Business Card

The business cards need to include:
Name
Title
Mailing Address
Phone Number
Web Address

Logo is attached. I would like white to be the primary color with incorporation of the company colors: #232D3A and #B5A451

Font styles to use
Other font styles liked:
• Montserrat, Avenir

Requirements
Must have
• Company Logo. No need to include the company name since the name is in the logo.
Should not have
• No line type designs

```html
<!DOCTYPE html>
<html lang="en">
<head>
<meta charset="UTF-8">
<title>KORVA Business Cards</title>
<link href="https://fonts.googleapis.com/css2?family=Montserrat:wght@400;500;600;700;800&display=swap" rel="stylesheet">
<style>
  :root {
    --navy: #232d3a;
    --gold: #b5a451;
    --white: #ffffff;
    --stage: #2a2a2b;
    --text: #1f2a37;
  }
  * { margin: 0; padding: 0; box-sizing: border-box; }
  html, body {
    width: 1200px;
    height: 800px;
    overflow: hidden;
    background: var(--stage);
    font-family: "Montserrat", sans-serif;
  }
  .canvas {
    width: 1200px;
    height: 800px;
    display: flex;
    align-items: center;
    justify-content: center;
    gap: 40px;
  }
  .card {
    position: relative;
    width: 540px;
    height: 310px;
    border-radius: 18px;
    overflow: hidden;
  }

  /* Front */
  .card-front {
    background: var(--white);
    color: var(--text);
  }
  .holder {
    position: absolute;
    left: 36px;
    top: 36px;
  }
  .holder-name {
    font-size: 19px;
    font-weight: 800;
    letter-spacing: 1px;
    color: var(--navy);
    text-transform: uppercase;
  }
  .holder-title {
    font-size: 12px;
    font-weight: 500;
    letter-spacing: 1px;
    color: var(--gold);
    text-transform: uppercase;
    margin-top: 1px;
  }
  .contact-list {
    position: absolute;
    left: 36px;
    top: 122px;
    width: 250px;
    list-style: none;
    font-size: 12.5px;
    font-weight: 500;
    line-height: 1.45;
    color: var(--navy);
  }
  .contact-item {
    display: flex;
    align-items: flex-start;
    gap: 10px;
    margin-bottom: 6px;
    white-space: nowrap;
  }
  .contact-icon {
    flex: 0 0 14px;
    width: 14px;
    height: 14px;
    margin-top: 2px;
    fill: var(--gold);
  }
  .front-brand {
    position: absolute;
    right: 36px;
    bottom: 74px;
    display: flex;
    align-items: center;
    gap: 10px;
  }
  .brand-name {
    font-weight: 700;
    font-size: 54px;
    letter-spacing: 3px;
    line-height: 1;
  }
  .front-brand .brand-name { color: var(--navy); font-size: 42px; letter-spacing: 2px; }
  .brand-square {
    width: 18px;
    height: 18px;
    background: var(--gold);
  }
  .front-brand .brand-square { width: 14px; height: 14px; }

  /* Back */
  .card-back {
    background: var(--navy);
  }
  .back-brand {
    position: absolute;
    left: 0;
    right: 0;
    top: 98px;
    display: flex;
    justify-content: center;
    align-items: center;
    gap: 14px;
  }
  .back-brand .brand-name { color: var(--white); font-size: 58px; }
  .back-band {
    position: absolute;
    left: 0;
    right: 0;
    bottom: 0;
    height: 56px;
    background: var(--gold);
    border-top: 4px solid var(--white);
    display: flex;
    align-items: center;
    padding-left: 36px;
  }
  .back-web {
    font-size: 14px;
    font-weight: 600;
    letter-spacing: 2px;
    color: var(--white);
    text-transform: uppercase;
  }
</style>
</head>
<body>
<main class="canvas">

  <section class="card card-front" aria-label="Business card front">
    <header class="holder">
      <h1 class="holder-name">Daniel Hart</h1>
      <p class="holder-title">Director</p>
    </header>

    <ul class="contact-list">
      <li class="contact-item">
        <svg class="contact-icon" viewBox="0 0 14 14" aria-hidden="true">
          <path d="M7 0.5a4.6 4.6 0 0 0-4.6 4.6C2.4 8.6 7 13.5 7 13.5s4.6-4.9 4.6-8.4A4.6 4.6 0 0 0 7 0.5zm0 6.4a1.8 1.8 0 1 1 0-3.6 1.8 1.8 0 0 1 0 3.6z"/>
        </svg>
        <span>118 Larkspur Street<br>Suite 210, Aldenport<br>MI 49621</span>
      </li>
      <li class="contact-item">
        <svg class="contact-icon" viewBox="0 0 14 14" aria-hidden="true">
          <path d="M3.1 0.8l2 2.6c.3.4.3.9-.1 1.2l-1 .9c.7 1.6 2 2.9 3.5 3.6l.9-1c.3-.4.9-.4 1.2-.1l2.6 2c.4.3.4.9.1 1.2l-1.2 1.3c-.6.6-1.5.8-2.3.4C5.6 11.6 2.4 8.4 1.100 5.200.700 4.400.900 3.500 1.500 2.900L2.800.700c.1-.1.2 0 .3.1z"/>
        </svg>
        <span>555-014-2786</span>
      </li>
      <li class="contact-item">
        <svg class="contact-icon" viewBox="0 0 14 14" aria-hidden="true">
          <path d="M1 3h12v8H1z M1.6 3.4L7 7.6l5.4-4.2" fill="none" stroke="#b5a451" stroke-width="1.4"/>
        </svg>
        <span>info@korvadevelopment.com</span>
      </li>
      <li class="contact-item">
        <svg class="contact-icon" viewBox="0 0 14 14" aria-hidden="true">
          <g fill="none" stroke="#b5a451" stroke-width="1.1">
            <circle cx="7" cy="7" r="6"/>
            <ellipse cx="7" cy="7" rx="2.6" ry="6"/>
            <path d="M1 7h12M2 3.8h10M2 10.2h10"/>
          </g>
        </svg>
        <span>www.korvadevelopment.com</span>
      </li>
    </ul>

    <div class="front-brand">
      <span class="brand-square" aria-hidden="true"></span>
      <span class="brand-name">KORVA</span>
    </div>
  </section>

  <section class="card card-back" aria-label="Business card back">
    <div class="back-brand">
      <span class="brand-square" aria-hidden="true"></span>
      <span class="brand-name">KORVA</span>
    </div>
    <footer class="back-band">
      <span class="back-web">www.korvadevelopment.com</span>
    </footer>
  </section>

</main>
</body>
</html>
```